Marketing materials for computer support company
trifolds, sign, and magnet
Thank you everyone for your submissions! They were all wonderful.
draft #18 is great - we will spend some time to more carefully review it and give some specific feedback later today. Thanks again
regarding draft #13 and draft #12, these are what we are looking for. The dark photo with the people we would like to go though. We are a small company and don't want to misrepresent that.
We are would use draft #12 for commercial services and draft #13 for residential. Is there anything that could be done to make them slightly different from each other inside though? If not, I'm sure we will find some content to fit - but if someone took one of each brochure, I don't want them to look identical other than the front and color. Maybe even just a different image in the middle of draft #12 where the laptop/wrench image is? Anyway, awesome work!
regarding draft #11, I prefer this to draft #5. Just something doesn't quite fit for me - I'll try to come up with something more specific. Thanks though - this is currently our 2nd favorite
regarding draft #10, I hadn't thought about it before, but I love how one brochure uses mostly blue, and the other uses mostly orange. I also like the flow of both of these. I can't tell if they are tri-fold though. But if you were wondering if we'd like the idea - we do!
-Wade
Also, if it helps, you can checkout what we liked / didn't like in our ongoing stationery / business card content!
Our contest link is: http://www.quintaloft.net/contests/business-card-template-company-stationery
so I will try to be more specific to assist until the unveil it - but bear with me, this is not my area :-) So blue and orange are preferable. Less gradients are better. Curves and circles that flow across the entire front or back for the residential tri-fold connecting the content areas is preferable. Same idea, but with straight angled boxes seems to be what I like on the business tri-fold. Pictures seem more important on the business one (based on existing designs that we have seen), residential can use illustrations in place of pictures. That's what I've got for now!
I just noticed this project is listed as "veiled" even though I did not choose to do so, so I apologize if you can not see the comparisons I am making between each others designs. I will contact support to fix this.
regarding draft #1, thank you for the submission. While I will make some remarks about what I would like to see in the layout, this set of documents is very much along the lines of what I am looking for. The 8.5x11 represents the content of the tri-fold and the magnet has room for a 1" x 3" label. I also like the use of blue! There is something plain about the actual layout though, in comparison to the angles used in draft #4 business tri-fold or curves of draft #4 residential. Thanks again for the submission!
regarding draft #2, I really like the use of our colors and thank you for the submission! I would like more photos as opposed to graphics such as the "help / mouse" or "laptop with stethoscope". I felt the overall feel was very busy and took up a lot of space without providing much room for content. I did like the use of our logo, but I'm ok with it taking up less room in exchange for a really clean look.
regarding draft #3, I like the nerdy magnet guy, but needs room for a 1"x3" thermal label and more room for our name / contact info
regarding draft #4, I like the look of the business tri-fold more than that of the residential. The graphic for the back especially. I think the colors on the residential need to be brighter and more playful. I think the idea of the business tri-fold having more straight lines and sharp angles, while the residential has more curves is great. Just the colors and overall look don't appeal to me. While neither of the magnets would fit a 1x3 label I LOVE how simple the magnet with our logo cutout looks - great idea!

```html
<!DOCTYPE html>
<html lang="en">
<head>
<meta charset="utf-8">
<title>Brightpath Computer Support – Trifold Set</title>
<link rel="stylesheet" href="https://fonts.googleapis.com/css2?family=Open+Sans:wght@400;600;700;800&display=swap">
<style>
  :root{
    --blue:#1f8fd6;
    --blue-dark:#15609b;
    --orange:#f5821f;
    --ink:#3a3a3a;
    --paper:#ffffff;
    --paper-grey:#eceff2;
    --stage:#e7e3dd;
    --caption:#6b6256;
  }
  *{box-sizing:border-box;margin:0;padding:0}
  html,body{width:1200px;height:682px;overflow:hidden}
  body{background:var(--stage);font-family:"Open Sans",Arial,sans-serif;color:var(--ink);position:relative}
  .caption{position:absolute;font-size:9px;color:var(--caption);white-space:nowrap}
  .sheet{position:absolute;background:var(--paper);box-shadow:0 3px 10px rgba(0,0,0,.25);overflow:hidden}
  .sheet>svg{position:absolute;inset:0;width:100%;height:100%}
  .t{position:absolute;line-height:1.2}
  .brand{display:flex;align-items:center;gap:4px;font-weight:700;color:var(--blue-dark);font-size:8px;line-height:1.1;white-space:nowrap}
  .brand i{display:block;flex:none;width:9px;height:9px;background:var(--orange)}
  .headline{font-weight:800;color:var(--blue);font-size:13px}
  .sub{font-weight:700;color:var(--orange);font-size:5px;letter-spacing:.3px}
  .body{font-size:5px;color:#666;line-height:1.5}
  .phone{font-weight:700;color:var(--blue-dark);font-size:6px}
  .web{font-size:5px;color:#666}
  .band-text{font-weight:700;color:#fff;font-size:17px;line-height:1.15}
  .list{list-style:none;font-size:6px;color:#fff;line-height:1.8}
  .list li::before{content:"";display:inline-block;width:4px;height:4px;background:#fff;margin-right:4px;vertical-align:middle}
  .cover .brand{left:8%;top:5%}
  .cover .headline{left:8%;top:63%}
  .cover .sub{left:8%;top:69.5%}
  .cover .phone{left:8%;top:78%}
  .cover .web{left:8%;top:82.5%}
</style>
</head>
<body>

<!-- Residential services trifold, face -->
<p class="caption" style="left:31px;top:10px">residential services trifold - face</p>
<section class="sheet residential-face" style="left:31px;top:24px;width:425px;height:331px">
  <svg viewBox="0 0 425 331" preserveAspectRatio="none">
    <defs>
      <linearGradient id="towerTone" x1="0" y1="0" x2="1" y2="1"><stop offset="0" stop-color="#9aa3ab"/><stop offset="1" stop-color="#2e3338"/></linearGradient>
      <linearGradient id="keysTone" x1="0" y1="0" x2="1" y2="1"><stop offset="0" stop-color="#3f5f80"/><stop offset="1" stop-color="#14253a"/></linearGradient>
    </defs>
    <rect x="142" y="0" width="142" height="160" fill="var(--paper-grey)"/>
    <g role="img" aria-label="Photo of a desktop computer tower">
      <rect x="10" y="110" width="120" height="205" fill="url(#towerTone)"/>
    </g>
    <g role="img" aria-label="Photo of a technician at a computer keyboard">
      <polygon points="142,170 425,150 425,331 142,331" fill="url(#keysTone)"/>
    </g>
    <polygon points="284,72 425,60 425,135 284,145" fill="var(--blue)"/>
    <polygon points="142,160 425,138 425,150 142,170" fill="var(--orange)"/>
    <rect x="152" y="22" width="118" height="70" fill="var(--orange)"/>
    <rect x="0" y="320" width="142" height="11" fill="var(--blue)"/>
  </svg>
  <div class="t headline" style="left:8px;top:12px">LOREM IPSUM</div>
  <div class="t sub" style="left:8px;top:30px">AT HOME SERVICE</div>
  <div class="t body" style="left:8px;top:42px;width:120px">Fast friendly help at home for every device you own.</div>
  <ul class="t list" style="left:160px;top:30px">
    <li>Virus removal</li><li>Data backup</li><li>Network setup</li><li>Repairs</li>
  </ul>
  <div class="t brand" style="left:296px;top:20px;font-size:9px"><i></i><span>Brightpath<br>Computer Support</span></div>
  <div class="t band-text" style="left:296px;top:82px">Lorem Ipsum<br>software like</div>
</section>

<!-- One sided version -->
<p class="caption" style="left:538px;top:58px">one sided version</p>
<section class="sheet cover" style="left:533px;top:72px;width:134px;height:288px">
  <svg viewBox="0 0 130 283" preserveAspectRatio="none">
    <defs><linearGradient id="circuitTone" x1="0" y1="0" x2="1" y2="1"><stop offset="0" stop-color="#2f7f8a"/><stop offset="1" stop-color="#163b46"/></linearGradient></defs>
    <polygon points="0,56 46,56 0,92" fill="var(--orange)"/>
    <polygon points="0,72 130,52 130,64 0,86" fill="var(--blue)"/>
    <g role="img" aria-label="Photo of a hand working on a circuit board"><polygon points="0,86 130,64 130,140 0,160" fill="url(#circuitTone)"/></g>
    <polygon points="0,160 130,140 130,150 0,172" fill="var(--blue)"/>
    <polygon points="0,283 0,262 70,283" fill="var(--orange)"/>
    <polygon points="60,283 130,252 130,283" fill="var(--blue)"/>
  </svg>
  <div class="t brand"><i></i><span>Brightpath<br>Computer Support</span></div>
  <div class="t headline">LOREM IPSUM</div>
  <div class="t sub">YOUR SUBTITLE HERE</div>
  <div class="t phone">(555) 010 0199</div>
  <div class="t web">www.brightpathpc.com</div>
</section>

<!-- Business services trifold, face -->
<p class="caption" style="left:787px;top:58px">business services trifold - face</p>
<section class="sheet business-face" style="left:787px;top:72px;width:389px;height:283px">
  <svg viewBox="0 0 389 283" preserveAspectRatio="none">
    <defs>
      <linearGradient id="deskTone" x1="0" y1="0" x2="1" y2="1"><stop offset="0" stop-color="#4f6b84"/><stop offset="1" stop-color="#1c2d3d"/></linearGradient>
      <linearGradient id="circuitTone2" x1="0" y1="0" x2="1" y2="1"><stop offset="0" stop-color="#2f7f8a"/><stop offset="1" stop-color="#163b46"/></linearGradient>
    </defs>
    <g role="img" aria-label="Photo of office server equipment">
      <polygon points="0,190 130,165 130,283 0,283" fill="url(#deskTone)"/>
      <polygon points="130,165 259,140 259,283 130,283" fill="url(#deskTone)"/>
    </g>
    <g role="img" aria-label="Photo of a hand using tools on computer hardware">
      <polygon points="150,70 259,52 259,120 150,138" fill="url(#circuitTone2)"/>
    </g>
    <polygon points="0,180 259,130 259,140 0,190" fill="var(--orange)"/>
    <g transform="translate(259,0)">
      <polygon points="0,56 46,56 0,92" fill="var(--orange)"/>
      <polygon points="0,72 130,52 130,64 0,86" fill="var(--blue)"/>
      <g role="img" aria-label="Photo of a hand working on a circuit board"><polygon points="0,86 130,64 130,140 0,160" fill="url(#circuitTone2)"/></g>
      <polygon points="0,160 130,140 130,150 0,172" fill="var(--blue)"/>
      <polygon points="0,283 0,262 70,283" fill="var(--orange)"/>
      <polygon points="60,283 130,252 130,283" fill="var(--blue)"/>
    </g>
  </svg>
  <div class="t headline" style="left:8px;top:10px;font-size:11px">LOREM IPSUM</div>
  <div class="t sub" style="left:8px;top:26px">OUR SERVICES</div>
  <div class="t body" style="left:8px;top:36px;width:112px">Reliable support for offices, servers and networks of any size.</div>
  <div class="t sub" style="left:8px;top:70px">WHY CHOOSE US</div>
  <div class="t body" style="left:140px;top:12px;width:110px">Planned maintenance keeps your team working without costly downtime.</div>
  <div class="t brand" style="left:269px;top:12px"><i></i><span>Brightpath<br>Computer Support</span></div>
  <div class="t headline" style="left:269px;top:178px">LOREM IPSUM</div>
  <div class="t sub" style="left:269px;top:196px">YOUR SUBTITLE HERE</div>
  <div class="t phone" style="left:269px;top:220px">(555) 010 0199</div>
  <div class="t web" style="left:269px;top:233px">www.brightpathpc.com</div>
</section>

<!-- Residential trifold, front panel -->
<p class="caption" style="left:96px;top:370px">residential services trifold - presentation</p>
<section class="sheet residential-front" style="left:96px;top:384px;width:108px;height:250px">
  <svg viewBox="0 0 108 250" preserveAspectRatio="none">
    <defs><linearGradient id="keysTone2" x1="0" y1="0" x2="1" y2="1"><stop offset="0" stop-color="#3f5f80"/><stop offset="1" stop-color="#14253a"/></linearGradient></defs>
    <polygon points="0,56 108,46 108,100 0,108" fill="var(--blue)"/>
    <polygon points="0,108 108,100 108,108 0,116" fill="var(--orange)"/>
    <g role="img" aria-label="Photo of a technician at a computer keyboard"><polygon points="0,116 108,108 108,250 0,250" fill="url(#keysTone2)"/></g>
  </svg>
  <div class="t brand" style="left:8px;top:14px;font-size:7px"><i></i><span>Brightpath<br>Computer Support</span></div>
  <div class="t band-text" style="left:8px;top:62px;font-size:13px">Lorem Ipsum<br>software like</div>
</section>

<!-- Business trifold, front panel -->
<p class="caption" style="left:912px;top:372px">business services trifold - presentation</p>
<section class="sheet cover" style="left:912px;top:386px;width:120px;height:250px">
  <svg viewBox="0 0 130 283" preserveAspectRatio="none">
    <defs><linearGradient id="circuitTone3" x1="0" y1="0" x2="1" y2="1"><stop offset="0" stop-color="#2f7f8a"/><stop offset="1" stop-color="#163b46"/></linearGradient></defs>
    <polygon points="0,56 46,56 0,92" fill="var(--orange)"/>
    <polygon points="0,72 130,52 130,64 0,86" fill="var(--blue)"/>
    <g role="img" aria-label="Photo of a hand working on a circuit board"><polygon points="0,86 130,64 130,140 0,160" fill="url(#circuitTone3)"/></g>
    <polygon points="0,160 130,140 130,150 0,172" fill="var(--blue)"/>
    <polygon points="0,283 0,262 70,283" fill="var(--orange)"/>
    <polygon points="60,283 130,252 130,283" fill="var(--blue)"/>
  </svg>
  <div class="t brand" style="font-size:7px"><i></i><span>Brightpath<br>Computer Support</span></div>
  <div class="t headline" style="font-size:11px">LOREM IPSUM</div>
  <div class="t sub">YOUR SUBTITLE HERE</div>
  <div class="t phone">(555) 010 0199</div>
  <div class="t web">www.brightpathpc.com</div>
</section>

</body>
</html>
```